New (old) Business Card Design Project

I would like to purchase a customized version of a design you have previously submitted - https://www.artboardhub.example/design/7305816

I like the card above, and would like to use the same design, jus with my business name, CARRINGFORD ASSET ADVISORY. I like the colors in the card above, as well as the font. The other side will have my name, company name, address, phone, email, website, plus disclosure text I will provide.

Target Market(s)

wealthy families

Industry/Entity Type

Financial Services

Contact Information for Business Card

logo on one side, on other my name, company, address, phone, email, website, disclosure language I will provide.

Colors

Designer to choose colors to be used in the design.

Requirements
Must have
• colors: Deep blue and white
Nice to have
• Please see the items I have uploaded, below.
Should not have
• Cheap, tacky look.

```html
<!DOCTYPE html>
<html lang="en">
<head>
<meta charset="utf-8">
<title>Carringford Asset Advisory – Business Card</title>
<link rel="stylesheet" href="https://fonts.googleapis.com/css2?family=Montserrat:wght@400;500;600&display=swap">
<style>
  :root {
    --navy: #0b2160;
    --navy-text: #13296b;
    --white: #ffffff;
    --grey-text: #4a4f5c;
    --rule: #b9bfcf;
    --backdrop: #e4e5e8;
  }
  * { margin: 0; padding: 0; box-sizing: border-box; }
  html, body {
    width: 1200px;
    height: 960px;
    overflow: hidden;
    background: var(--backdrop);
    font-family: "Montserrat", Arial, sans-serif;
  }
  .sheet {
    width: 1200px;
    height: 960px;
    display: flex;
    flex-direction: column;
    align-items: center;
    justify-content: center;
    gap: 28px;
  }
  .card {
    width: 770px;
    height: 440px;
    position: relative;
    box-shadow: 0 6px 18px rgba(0, 0, 0, 0.18);
  }
  .card--front { background: var(--white); }
  .card--back {
    background: var(--navy);
    display: flex;
    align-items: center;
    justify-content: center;
  }
  .brand-name {
    font-weight: 500;
    letter-spacing: 0.16em;
    text-transform: uppercase;
    white-space: nowrap;
  }
  .card--front .brand-name {
    position: absolute;
    top: 62px;
    left: 58px;
    font-size: 22px;
    color: var(--navy-text);
  }
  .card--back .brand-name {
    font-size: 30px;
    color: var(--white);
  }
  .holder {
    position: absolute;
    left: 58px;
    right: 58px;
    bottom: 52px;
  }
  .holder-name {
    font-size: 34px;
    font-weight: 600;
    letter-spacing: 0.04em;
    color: var(--navy-text);
    line-height: 1.1;
  }
  .holder-title {
    font-size: 18px;
    font-weight: 400;
    letter-spacing: 0.04em;
    color: var(--grey-text);
    margin-top: 4px;
  }
  .holder-rule {
    border: 0;
    height: 1.5px;
    background: var(--rule);
    margin: 14px 0 16px;
  }
  .contact-line {
    font-size: 17px;
    color: var(--grey-text);
    line-height: 1.55;
    white-space: nowrap;
  }
  .contact-label { color: var(--navy-text); }
  .contact-link { color: var(--navy-text); }
</style>
</head>
<body>
  <main class="sheet">
    <section class="card card--front" aria-label="Card front">
      <div class="brand-name">Carringford Asset Advisory</div>
      <div class="holder">
        <p class="holder-name">DANIEL HARTLEY</p>
        <p class="holder-title">MANAGING DIRECTOR</p>
        <hr class="holder-rule">
        <p class="contact-line"><span class="contact-label">TEL:</span> XXX XXX XXXX | <span class="contact-label">FAX:</span> XXX XXX XXXX</p>
        <p class="contact-line"><span class="contact-label">EMAIL:</span> daniel@carringfordadvisory.example | <span class="contact-link">www.carringfordadvisory.example</span></p>
      </div>
    </section>
    <section class="card card--back" aria-label="Card back">
      <div class="brand-name">Carringford Asset Advisory</div>
    </section>
  </main>
</body>
</html>
```